Election features for a political website

The Hearthside Ledger (www.hearthsideledger.example)
Web banner designs
Please have a look at The Hearthside Ledger website (www.hearthsideledger.example). We are seeking to add an advertising style banner at the top of every page and post. It will run right across the page (1024 pixels) and be in the region of 200 pixels vertically. (Please advise on what looks best size wise.
The banner will be a slider, operated in a similar way to the current homepage slider. There will be four items on the slider, and so we need four designs that match the aesthetic feel of the website. Each slider will link through to posts on the website.
1.
Headline: OUR CANDIDATE OF THE DAY
Space for a name, head and shoulders picture of the person to be dropped in and a one line reason. This will need to be in an editable format as this image will be changed each day for one month.
2.
Headline: HERO OF THE DAY
Space for name and a one line reason. This will need to be in an editable format as this image will be changed each day for one month.
3.
Headline: VILLAIN OF THE DAY
Space for name of the person to be dropped in and a one line reason. This will need to be in an editable format as this image will be changed each day for one month.
4.
Headline: THL Poll – [Date]
If the election was today, who would you vote for?
Clickable options:
Brightfolders
Ashvel
Marden Alliancers
Vornu
Tally
Other
Can a poll widget be added to the banner? We would like this poll to reset each day and then pool the results into a graph day by day over a one month period.
Reason: Payment is now guaranteed. We would like to see more options.

```html
<!DOCTYPE html>
<html lang="en">
<head>
<meta charset="utf-8">
<title>Hero of the day – The Hearthside Ledger banner</title>
<link rel="stylesheet" href="https://fonts.googleapis.com/css2?family=EB+Garamond:wght@400&family=Fira+Sans+Extra+Condensed:wght@800&display=swap">
<style>
  :root {
    --banner-bg: #000000;
    --headline-bg: #05568d;
    --text-light: #ffffff;
    --portrait-light: #e6e9ec;
    --portrait-mid: #9ea4aa;
    --portrait-dark: #15171a;
  }
  html, body {
    margin: 0;
    padding: 0;
    width: 1200px;
    height: 234px;
    overflow: hidden;
    background: var(--banner-bg);
  }
  .banner {
    position: relative;
    width: 1200px;
    height: 234px;
    background: var(--banner-bg);
    overflow: hidden;
  }
  .banner__portrait {
    position: absolute;
    left: 0;
    top: 0;
    width: 370px;
    height: 234px;
    background:
      linear-gradient(180deg, rgba(0,0,0,0) 55%, rgba(20,22,26,0.85) 100%),
      linear-gradient(90deg, var(--portrait-light) 0%, var(--portrait-mid) 35%, var(--portrait-dark) 62%, var(--portrait-light) 78%, var(--portrait-mid) 100%);
  }
  .banner__headline {
    position: absolute;
    left: 324px;
    top: 0;
    width: 414px;
    height: 110px;
    background: var(--headline-bg);
    box-sizing: border-box;
    padding: 24px 0 0 32px;
  }
  .banner__title {
    margin: 0;
    font-family: "Fira Sans Extra Condensed", "Arial Narrow", sans-serif;
    font-weight: 800;
    font-size: 58px;
    line-height: 60px;
    color: var(--text-light);
    white-space: nowrap;
  }
  .banner__reason {
    position: absolute;
    left: 404px;
    top: 121px;
    margin: 0;
    font-family: "EB Garamond", Garamond, serif;
    font-size: 19.5px;
    line-height: 26px;
    color: var(--text-light);
  }
  .banner__reason-line {
    display: block;
    white-space: nowrap;
  }
</style>
</head>
<body>
  <a class="banner" href="#" aria-label="Hero of the day">
    <div class="banner__portrait" role="img" aria-label="Head and shoulders portrait of today's hero, in a dark suit against a light office background"></div>
    <div class="banner__headline">
      <h1 class="banner__title">Hero of the day</h1>
    </div>
    <p class="banner__reason">
      <span class="banner__reason-line">Ucillis aut adi idest, volupiderio beatiistes eum init ex et ut evendit inctem eic</span>
      <span class="banner__reason-line">tessitem asitiam vollaut officab oritas audae nonsequ iantion Quia sum harum</span>
      <span class="banner__reason-line">volenis eatent, ut di dolupta quae si id magnimi, occusaessit, consed quatibus</span>
    </p>
  </a>
</body>
</html>
```